Building company buisness cards

We are looking for a sharp modern new look for our business cards.We are a New Zealand based company that specialises in house and land packages.We have attached a photo of the current logo and would like to see if it can be improved somehow if needed.We are open to any colours but we have chosen Black and White at this stage. Feel free to change the font and make the logo smarter looking.Play with the colours and see what looks best.We want a card that looks so good know one will want to throw it away!

Target Market(s)

Building profesonals, home buyers

Industry/Entity Type

Building

Contact Information for Business Card

Derek Haskins
0274930268
derekh@stonerange.co.nz

Font styles to use
Serif
Sans Serif

Colors

Designer to choose colors to be used in the design.

Requirements
Must have
• Just the logo on one side and details on the other
• Clean simple looking card
Nice to have
• Round corners and detail like raised or spot UV
• Something that stands out
Should not have
• To title needed, Director etc

```html
<!DOCTYPE html>
<html lang="en">
<head>
<meta charset="utf-8">
<title>Stonerange Business Cards</title>
<link href="https://fonts.googleapis.com/css2?family=Libre+Baskerville&family=Jost:wght@400;500&display=swap" rel="stylesheet">
<style>
  :root {
    --page: #ffffff;
    --ink-dark: #2f3338;
    --ink-light: #ffffff;
    --front-top: #3a3f45;
    --front-mid: #23272b;
    --front-bottom: #060707;
    --back-top: #ffffff;
    --back-mid: #eeeeef;
    --back-bottom: #d9dadb;
    --icon: #3c4045;
    --divider: rgba(0,0,0,0.08);
  }
  html, body { margin: 0; padding: 0; overflow: hidden; }
  body { width: 1200px; height: 902px; background: var(--page); position: relative; }
  .card { position: absolute; overflow: hidden; }
  .card-front { left: 343px; top: 155px; width: 519px; height: 296px; }
  .card-back { left: 347px; top: 493px; width: 515px; height: 292px; }
  .card-texture { position: absolute; inset: 0; }
  .card-front .card-texture {
    background:
      linear-gradient(180deg, rgba(255,255,255,0.05) 0%, rgba(255,255,255,0) 48%, rgba(255,255,255,0.06) 49%, rgba(0,0,0,0) 52%),
      linear-gradient(180deg, var(--front-top) 0%, var(--front-mid) 50%, var(--front-bottom) 100%);
  }
  .card-back .card-texture {
    background:
      linear-gradient(135deg, rgba(255,255,255,0.6) 0%, rgba(255,255,255,0) 40%),
      linear-gradient(180deg, var(--back-top) 0%, var(--back-mid) 45%, var(--back-top) 55%, var(--back-bottom) 100%);
  }
  .brand { position: absolute; text-align: center; }
  .brand-name {
    font-family: "Libre Baskerville", Georgia, serif;
    font-size: 40px; line-height: 1; letter-spacing: -0.5px;
    display: block;
  }
  .brand-tagline {
    font-family: "Jost", Arial, sans-serif; font-weight: 500;
    font-size: 10px; letter-spacing: -0.1px; display: block; margin-top: 6px;
  }
  .card-front .brand { left: 0; right: 0; top: 123px; color: var(--ink-light); }
  .card-back .brand { left: 14px; width: 240px; top: 130px; color: var(--ink-dark); }
  .card-back .brand-name { font-size: 34px; }
  .divider { position: absolute; left: 260px; top: 40px; width: 1px; height: 220px; background: var(--divider); }
  .contact-list { position: absolute; left: 290px; top: 96px; margin: 0; padding: 0; list-style: none; }
  .contact-item {
    display: flex; align-items: center; height: 28px; margin-bottom: 12px;
    font-family: "Jost", Arial, sans-serif; font-size: 14px; color: var(--ink-dark);
    white-space: nowrap;
  }
  .contact-item svg { width: 28px; height: 28px; margin-right: 7px; flex: none; }
  .contact-item.phone { font-size: 13px; }
  .contact-item.web { font-size: 15px; }
</style>
</head>
<body>
  <section class="card card-front">
    <div class="card-texture" role="img" aria-label="Dark charcoal diamond tile pattern"></div>
    <div class="brand">
      <span class="brand-name">Stonerange</span>
      <span class="brand-tagline">BUILT AROUND YOUR LIFE</span>
    </div>
  </section>

  <section class="card card-back">
    <div class="card-texture" role="img" aria-label="Light grey diamond tile pattern"></div>
    <div class="brand">
      <span class="brand-name">Stonerange</span>
      <span class="brand-tagline">BUILT AROUND YOUR LIFE</span>
    </div>
    <div class="divider"></div>
    <ul class="contact-list">
      <li class="contact-item email">
        <svg viewBox="0 0 28 28"><circle cx="14" cy="14" r="14" fill="var(--icon)"/><rect x="7.5" y="9.5" width="13" height="9" fill="none" stroke="#fff" stroke-width="1.4"/><path d="M7.5 9.5 L14 15 L20.5 9.5" fill="none" stroke="#fff" stroke-width="1.4"/></svg>
        derekh@stonerange.co.nz
      </li>
      <li class="contact-item phone">
        <svg viewBox="0 0 28 28"><circle cx="14" cy="14" r="14" fill="var(--icon)"/><path d="M10 7.5c.8-.4 1.6 0 2 .8l1 2.2c.3.7 0 1.3-.5 1.7l-.9.7c.6 1.6 1.8 2.9 3.4 3.7l.8-.9c.5-.5 1.100-.7 1.700-.4l2.2 1.100c.8.4 1.100 1.200.7 2l-.6 1c-.6 1-1.900 1.400-3 1-4.300-1.600-7.400-4.800-8.800-9.100-.3-1.100.1-2.300 1-2.900z" fill="#fff"/></svg>
        CELL: 0274930268
      </li>
      <li class="contact-item web">
        <svg viewBox="0 0 28 28"><circle cx="14" cy="14" r="14" fill="var(--icon)"/><circle cx="14" cy="14" r="7" fill="none" stroke="#fff" stroke-width="1.4"/><ellipse cx="14" cy="14" rx="3" ry="7" fill="none" stroke="#fff" stroke-width="1.2"/><line x1="7" y1="14" x2="21" y2="14" stroke="#fff" stroke-width="1.2"/></svg>
        WWW.Stonerange.co.nz/
      </li>
    </ul>
  </section>
</body>
</html>
```